Data Management as a Service Powerpoint Design

We need the attached PowerPoint presentation redesigning including all graphics, icons, images, and graphs. The messaging in the content should remain however artistic flair can be used to change any diagram/icon/graph layout.
For preferred colour scheme and brand continuity our website is: tavexo.com, however we are open to new colours/scheme.
The only stipulation is that the hexagon layout on the DMaaS product slide (slide 4) must remain. All other icons must be changed. We would also like this to be editable, and not full-slide static images pasted from another graphics suite.

```html
<!DOCTYPE html>
<html lang="en">
<head>
<meta charset="utf-8">
<title>Tavexo – Data Management as a Service</title>
<link href="https://fonts.googleapis.com/css2?family=Montserrat:wght@400;500;600;700;800&display=swap" rel="stylesheet">
<style>
:root{
  --canvas:#cbcbcb;
  --orange:#ef7232;
  --orange-deep:#e05a1f;
  --ink:#2f2f2f;
  --grey:#8d8d8d;
  --grey-light:#b9b9b9;
  --paper:#f5f5f5;
  --navy:#0a1e4a;
}
*{margin:0;padding:0;box-sizing:border-box}
html,body{width:1200px;height:1124px;overflow:hidden;background:var(--canvas);font-family:"Montserrat",sans-serif}
.deck{position:relative;width:1200px;height:1124px}
.slide{position:absolute;width:541px;height:304px;box-shadow:0 14px 18px -8px rgba(0,0,0,.35);background:var(--paper);overflow:hidden}
.slide svg{display:block;width:100%;height:100%}
.slide--title{left:42px;top:75px}
.slide--volume{left:614px;top:75px}
.slide--application{left:42px;top:409px}
.slide--dmaas{left:616px;top:412px}
.slide--architecture{left:42px;top:744px}
.slide--lifecycle{left:616px;top:741px}
text{font-family:"Montserrat",sans-serif}
.footer-site{fill:#fff;font-weight:600;font-size:22px}
.footer-num{fill:#fff;font-weight:700;font-size:22px}
.tag-text{fill:#fff;font-weight:600;font-size:22px}
.axis-small{fill:#555;font-size:7px}
.point-label{fill:#333;font-size:7.5px}
.reg{fill:#333;font-size:12.5px}
.reg-line{stroke:#888;stroke-width:1;stroke-dasharray:3 2;fill:none}
.card-label{fill:#3a3a3a;font-weight:600;font-size:29px}
.hex-label{fill:#3a3a3a;font-weight:500;font-size:24px}
.box-label{fill:#333;font-weight:600;font-size:20px}
.small-bold{fill:#333;font-weight:700;font-size:15px}
.heading-bold{fill:#444;font-weight:700;font-size:20px}
</style>
</head>
<body>
<div class="deck">

<!-- Title slide -->
<section class="slide slide--title">
<svg viewBox="0 0 897 504" aria-label="Title slide">
  <defs>
    <linearGradient id="serverGlow" x1="0" y1="0" x2="1" y2="1">
      <stop offset="0" stop-color="#0f2f6e"/>
      <stop offset=".5" stop-color="#0a2a66"/>
      <stop offset="1" stop-color="#06112e"/>
    </linearGradient>
  </defs>
  <rect width="897" height="504" fill="url(#serverGlow)" role="img" aria-label="Photograph of a blue-lit data centre server corridor"/>
  <rect x="0" y="272" width="640" height="192" fill="rgba(5,15,40,.35)"/>
  <text x="30" y="68" fill="#fff" font-weight="700" font-size="50" letter-spacing="3">TAVEXO</text>
  <text x="34" y="336" fill="#fff" font-weight="800" font-size="58" style="font-variant:small-caps">Data Management</text>
  <text x="34" y="400" fill="#fff" font-weight="800" font-size="58" style="font-variant:small-caps">as a Service</text>
  <text x="34" y="448" fill="#fff" font-weight="600" font-size="22">www.tavexo.com</text>
</svg>
</section>

<!-- Data volume slide -->
<section class="slide slide--volume">
<svg viewBox="0 0 897 504" aria-label="Data volume chart slide">
  <defs>
    <marker id="arrowOrange" viewBox="0 0 6 6" refX="5" refY="3" markerWidth="5" markerHeight="5" orient="auto"><path d="M0,0L6,3L0,6z" fill="var(--orange)"/></marker>
  </defs>
  <rect width="897" height="504" fill="var(--paper)"/>
  <polygon points="36,56 48,36 72,36 84,56 72,76 48,76" fill="#fff" stroke="#555" stroke-width="2"/>
  <polygon points="79,33 759,33 759,79 79,79 92,56" fill="var(--orange)"/>
  <text class="tag-text" x="99" y="64" font-size="21" textLength="645" lengthAdjust="spacingAndGlyphs">Volume of data created and replicated worldwide (source: Korva)</text>

  <g class="chart">
    <g stroke="#ddd" stroke-width="1">
      <line x1="67" y1="95" x2="830" y2="95"/><line x1="67" y1="110" x2="830" y2="110"/><line x1="67" y1="126" x2="830" y2="126"/><line x1="67" y1="141" x2="830" y2="141"/><line x1="67" y1="157" x2="830" y2="157"/><line x1="67" y1="172" x2="830" y2="172"/><line x1="67" y1="187" x2="830" y2="187"/><line x1="67" y1="203" x2="830" y2="203"/><line x1="67" y1="218" x2="830" y2="218"/><line x1="67" y1="234" x2="830" y2="234"/>
    </g>
    <line x1="67" y1="92" x2="67" y2="249" stroke="#777"/>
    <line x1="67" y1="249" x2="830" y2="249" stroke="#777"/>
    <g class="axis-small" text-anchor="end">
      <text x="62" y="98">200</text><text x="62" y="113">180</text><text x="62" y="129">160</text><text x="62" y="144">140</text><text x="62" y="160">120</text><text x="62" y="175">100</text><text x="62" y="190">80</text><text x="62" y="206">60</text><text x="62" y="221">40</text><text x="62" y="237">20</text><text x="62" y="252">0</text>
    </g>
    <text class="axis-small" font-size="6" transform="translate(40,216) rotate(-90)">Data Volume in Zettabytes</text>
    <polyline fill="none" stroke="var(--orange)" stroke-width="2" points="77,249 101.8,249 126.7,249 151.5,249 176.3,249 201.2,248.2 226,248.2 250.8,248.2 275.7,248.2 300.5,248.2 325.3,248.2 350.2,248.2 375,248.2 399.8,248.2 424.7,247.5 449.5,247.5 474.3,245.2 499.2,243.6 524,242.1 548.8,239 573.7,236.7 598.5,235.1 623.3,229 648.2,223.6 673,217.4 697.8,199.7 722.7,188.2 747.5,174.3 772.3,156.6 797.2,135.8 822,109.6"/>
    <g class="point-label" text-anchor="middle">
      <text x="77" y="231">0</text><text x="101.8" y="231">0</text><text x="126.7" y="231">0</text><text x="151.5" y="231">0</text><text x="176.3" y="231">0</text><text x="201.2" y="230">1</text><text x="226" y="230">1</text><text x="250.8" y="230">1</text><text x="275.7" y="230">1</text><text x="300.5" y="230">1</text><text x="325.3" y="230">1</text><text x="350.2" y="220">1</text><text x="375" y="217">1</text><text x="399.8" y="212">1</text><text x="424.7" y="209">2</text><text x="449.5" y="213">2</text><text x="474.3" y="222">5</text><text x="499.2" y="226">7</text><text x="524" y="221">9</text><text x="548.8" y="216">13</text><text x="573.7" y="208">16</text><text x="598.5" y="200">18</text><text x="623.3" y="193">26</text><text x="648.2" y="186">33</text><text x="673" y="191">41</text><text x="697.8" y="196">64</text><text x="722.7" y="184">79</text><text x="747.5" y="168">97</text><text x="772.3" y="149">120</text><text x="797.2" y="129">147</text><text x="810" y="108">181</text>
    </g>
    <g class="axis-small" font-size="6.5">
      <text transform="translate(80,275) rotate(-90)">1995</text><text transform="translate(104.8,275) rotate(-90)">1996</text><text transform="translate(129.7,275) rotate(-90)">1997</text><text transform="translate(154.5,275) rotate(-90)">1998</text><text transform="translate(179.3,275) rotate(-90)">1999</text><text transform="translate(204.2,275) rotate(-90)">2000</text><text transform="translate(229,275) rotate(-90)">2001</text><text transform="translate(253.8,275) rotate(-90)">2002</text><text transform="translate(278.7,275) rotate(-90)">2003</text><text transform="translate(303.5,275) rotate(-90)">2004</text><text transform="translate(328.3,275) rotate(-90)">2005</text><text transform="translate(353.2,275) rotate(-90)">2006</text><text transform="translate(378,275) rotate(-90)">2007</text><text transform="translate(402.8,275) rotate(-90)">2008</text><text transform="translate(427.7,275) rotate(-90)">2009</text><text transform="translate(452.5,275) rotate(-90)">2010</text><text transform="translate(477.3,275) rotate(-90)">2011</text><text transform="translate(502.2,275) rotate(-90)">2012</text><text transform="translate(527,275) rotate(-90)">2013</text><text transform="translate(551.8,275) rotate(-90)">2014</text><text transform="translate(576.7,275) rotate(-90)">2015</text><text transform="translate(601.5,275) rotate(-90)">2016</text><text transform="translate(626.3,275) rotate(-90)">2017</text><text transform="translate(651.2,275) rotate(-90)">2018</text><text transform="translate(676,275) rotate(-90)">2019</text><text transform="translate(700.8,275) rotate(-90)">2020</text><text transform="translate(725.7,275) rotate(-90)">2021</text><text transform="translate(750.5,275) rotate(-90)">2022</text><text transform="translate(775.3,275) rotate(-90)">2023</text><text transform="translate(800.2,275) rotate(-90)">2024</text><text transform="translate(825,275) rotate(-90)">2025</text>
    </g>
  </g>

  <g class="regulations">
    <text class="reg" x="67" y="303">UK DPA 1984  UK DPA</text>
    <line class="reg-line" x1="208" y1="299" x2="385" y2="299" marker-end="url(#arrowOrange)"/>
    <text class="reg" x="393" y="303">UK DPA 1998</text>
    <line class="reg-line" x1="475" y1="299" x2="625" y2="299" marker-end="url(#arrowOrange)"/>
    <text class="reg" x="633" y="303">UK DPA 2018</text>
    <line class="reg-line" x1="716" y1="299" x2="794" y2="299" marker-end="url(#arrowOrange)"/>

    <text class="reg" x="127" y="318">EU-US Safe Harbor</text>
    <line class="reg-line" x1="250" y1="314" x2="458" y2="314" marker-end="url(#arrowOrange)"/>
    <text class="reg" x="462" y="318">EU-US Privacy Shield</text>
    <line class="reg-line" x1="600" y1="314" x2="630" y2="314" marker-end="url(#arrowOrange)"/>
    <text class="reg" x="635" y="318">EU-US DPF</text>
    <line class="reg-line" x1="710" y1="314" x2="794" y2="314" marker-end="url(#arrowOrange)"/>

    <text class="reg" x="199" y="334">PERC</text><line class="reg-line" x1="240" y1="330" x2="794" y2="330" marker-end="url(#arrowOrange)"/>
    <text class="reg" x="211" y="350">ISO 27001</text><line class="reg-line" x1="280" y1="346" x2="794" y2="346" marker-end="url(#arrowOrange)"/>
    <text class="reg" x="249" y="366">PCI DSS</text><line class="reg-line" x1="305" y1="362" x2="794" y2="362" marker-end="url(#arrowOrange)"/>
    <text class="reg" x="291" y="382">SOC2</text><line class="reg-line" x1="335" y1="378" x2="794" y2="378" marker-end="url(#arrowOrange)"/>
    <text class="reg" x="305" y="397">ISO 27018</text><line class="reg-line" x1="375" y1="393" x2="794" y2="393" marker-end="url(#arrowOrange)"/>
    <text class="reg" x="333" y="412">Cyber Essentials</text><line class="reg-line" x1="440" y1="408" x2="794" y2="408" marker-end="url(#arrowOrange)"/>
    <text class="reg" x="399" y="427">ISO 27017</text><line class="reg-line" x1="475" y1="423" x2="794" y2="423" marker-end="url(#arrowOrange)"/>
    <text class="reg" x="399" y="442">Health Data Toolkit</text><line class="reg-line" x1="535" y1="438" x2="794" y2="438" marker-end="url(#arrowOrange)"/>
    <text class="reg" x="399" y="457">GDPR</text><line class="reg-line" x1="445" y1="453" x2="794" y2="453" marker-end="url(#arrowOrange)"/>
  </g>

  <rect y="463" width="897" height="41" fill="var(--orange)"/>
  <polygon points="20,504 32,504 70,463 58,463" fill="#fff"/>
  <text class="footer-site" x="68" y="492">www.tavexo.com</text>
  <text class="footer-num" x="834" y="492">1</text>
</svg>
</section>

<!-- Application slide -->
<section class="slide slide--application">
<svg viewBox="0 0 897 504" aria-label="Application slide">
  <defs>
    <linearGradient id="cardGrey" x1="0" y1="0" x2="1" y2="1">
      <stop offset="0" stop-color="#b4b4b4"/><stop offset=".5" stop-color="#dedede"/><stop offset="1" stop-color="#a9a9a9"/>
    </linearGradient>
  </defs>
  <rect width="897" height="504" fill="var(--paper)"/>
  <polygon points="36,56 48,36 72,36 84,56 72,76 48,76" fill="#fff" stroke="#555" stroke-width="2"/>
  <polygon points="80,33 240,33 240,79 80,79 92,56" fill="var(--orange)"/>
  <text class="tag-text" x="100" y="64" textLength="118" lengthAdjust="spacingAndGlyphs">Application</text>

  <g class="pillar">
    <rect x="48" y="195" width="248" height="140" rx="18" fill="url(#cardGrey)"/>
    <circle cx="172" cy="195" r="52" fill="#eee"/><circle cx="172" cy="195" r="45" fill="var(--orange)"/>
    <circle cx="172" cy="195" r="16" fill="none" stroke="#222" stroke-width="7" stroke-dasharray="6 3"/><circle cx="172" cy="195" r="6" fill="#222"/>
    <text class="card-label" x="172" y="293" text-anchor="middle">Automation</text>
  </g>
  <g class="pillar">
    <rect x="325" y="195" width="248" height="140" rx="18" fill="url(#cardGrey)"/>
    <circle cx="449" cy="195" r="52" fill="#eee"/><circle cx="449" cy="195" r="45" fill="var(--orange)"/>
    <path d="M428,200 a11,11 0 0 1 6,-20 a15,15 0 0 1 28,-2 a11,11 0 0 1 8,22 z" fill="#222"/>
    <path d="M438,200v12M449,200v16M460,200v12" stroke="#222" stroke-width="3"/>
    <text class="card-label" x="449" y="293" text-anchor="middle">AI</text>
  </g>
  <g class="pillar">
    <rect x="601" y="195" width="248" height="140" rx="18" fill="url(#cardGrey)"/>
    <circle cx="725" cy="195" r="52" fill="#eee"/><circle cx="725" cy="195" r="45" fill="var(--orange)"/>
    <circle cx="710" cy="182" r="6" fill="#222"/><circle cx="725" cy="180" r="6" fill="#222"/><circle cx="740" cy="182" r="6" fill="#222"/>
    <circle cx="725" cy="205" r="11" fill="none" stroke="#222" stroke-width="6" stroke-dasharray="5 3"/>
    <text class="card-label" x="725" y="293" text-anchor="middle">Service</text>
  </g>

  <rect y="463" width="897" height="41" fill="var(--orange)"/>
  <polygon points="20,504 32,504 70,463 58,463" fill="#fff"/>
  <text class="footer-site" x="68" y="492">www.tavexo.com</text>
  <text class="footer-num" x="834" y="492">2</text>
</svg>
</section>

<!-- DMaaS hexagon slide -->
<section class="slide slide--dmaas">
<svg viewBox="0 0 897 504" aria-label="DMaaS product slide">
  <defs>
    <linearGradient id="hexOrange" x1="0" y1="0" x2="0" y2="1">
      <stop offset="0" stop-color="var(--orange)"/><stop offset="1" stop-color="var(--orange-deep)"/>
    </linearGradient>
    <linearGradient id="iconHex" x1="0" y1="0" x2="1" y2="1">
      <stop offset="0" stop-color="#a5a5a5"/><stop offset="1" stop-color="#7a7a7a"/>
    </linearGradient>
  </defs>
  <rect width="897" height="504" fill="var(--paper)"/>
  <polyline points="332,36 212,244 330,446" fill="none" stroke="#444" stroke-width="1.5"/>
  <polyline points="564,36 684,244 566,446" fill="none" stroke="#444" stroke-width="1.5"/>
  <polygon points="230,244 339,56 557,56 668,244 557,433 339,433" fill="url(#hexOrange)"/>
  <polygon points="263,244 356,86 540,86 631,244 540,403 356,403" fill="#fff"/>
  <text x="446" y="270" text-anchor="middle" fill="var(--ink)" font-weight="700" font-size="72">DMaaS</text>

  <g class="feature">
    <polygon points="196,70 213,40 247,40 264,70 247,100 213,100" fill="url(#iconHex)"/>
    <rect x="219" y="70" width="22" height="6" fill="#fff"/><rect x="219" y="79" width="22" height="6" fill="#fff"/><circle cx="230" cy="58" r="8" fill="#fff"/>
    <text class="hex-label" x="188" y="79" text-anchor="end">EDRMS</text>
  </g>
  <g class="feature">
    <polygon points="116,246 133,216 167,216 184,246 167,276 133,276" fill="url(#iconHex)"/>
    <path d="M150,232 l12,5 v9 c0,8 -6,12 -12,15 c-6,-3 -12,-7 -12,-15 v-9z" fill="#fff"/><circle cx="150" cy="246" r="3" fill="#888"/>
    <text class="hex-label" x="150" y="304" text-anchor="middle">Privacy</text>
  </g>
  <g class="feature">
    <polygon points="198,413 215,383 249,383 266,413 249,443 215,443" fill="url(#iconHex)"/>
    <circle cx="232" cy="413" r="12" fill="none" stroke="#fff" stroke-width="4" stroke-dasharray="14 5"/>
    <text class="hex-label" x="190" y="421" text-anchor="end">Lifecycle</text>
  </g>
  <g class="feature">
    <polygon points="623,70 640,40 674,40 691,70 674,100 640,100" fill="url(#iconHex)"/>
    <circle cx="657" cy="70" r="7" fill="#fff"/><circle cx="644" cy="60" r="4" fill="#fff"/><circle cx="670" cy="60" r="4" fill="#fff"/><circle cx="644" cy="82" r="4" fill="#fff"/><circle cx="670" cy="82" r="4" fill="#fff"/>
    <path d="M644,60L670,82M670,60L644,82" stroke="#fff" stroke-width="2"/>
    <text class="hex-label" x="706" y="64">Data</text>
    <text class="hex-label" x="706" y="92">Mapping</text>
  </g>
  <g class="feature">
    <polygon points="719,240 736,210 770,210 787,240 770,270 736,270" fill="url(#iconHex)"/>
    <rect x="744" y="224" width="18" height="12" fill="#fff"/><path d="M753,236v8M740,248h26M740,244v8M766,244v8" stroke="#fff" stroke-width="2.5" fill="none"/>
    <text class="hex-label" x="760" y="294" text-anchor="middle">Classification</text>
  </g>
  <g class="feature">
    <polygon points="626,413 643,383 677,383 694,413 677,443 643,443" fill="url(#iconHex)"/>
    <rect x="650" y="398" width="20" height="27" rx="2" fill="#fff"/><path d="M654,407l3,3 5,-5M654,417l3,3 5,-5" stroke="#888" stroke-width="2" fill="none"/>
    <text class="hex-label" x="708" y="423">Assessment</text>
  </g>

  <rect y="463" width="897" height="41" fill="var(--orange)"/>
  <polygon points="20,504 32,504 70,463 58,463" fill="#fff"/>
  <text class="footer-site" x="68" y="492">www.tavexo.com</text>
  <text class="footer-num" x="834" y="492">3</text>
</svg>
</section>

<!-- Architecture slide -->
<section class="slide slide--architecture">
<svg viewBox="0 0 897 504" aria-label="Architecture and certifications slide">
  <defs>
    <linearGradient id="panelGrey" x1="0" y1="0" x2="0" y2="1">
      <stop offset="0" stop-color="#d2d2d2"/><stop offset="1" stop-color="#bcbcbc"/>
    </linearGradient>
  </defs>
  <rect width="897" height="504" fill="#fff"/>

  <text class="heading-bold" x="128" y="87" text-anchor="middle">Customer’s Public</text>
  <rect x="30" y="102" width="196" height="103" rx="14" fill="url(#panelGrey)" stroke="#e8e8e8" stroke-width="4"/>
  <rect x="78" y="135" width="22" height="30" rx="2" fill="#444"/><path d="M83,146l3,3 6,-6M83,156l3,3 6,-6" stroke="#ccc" stroke-width="2" fill="none"/>
  <ellipse cx="154" cy="140" rx="17" ry="5" fill="#444"/><rect x="137" y="140" width="34" height="26" fill="#444"/><path d="M137,150h34M137,158h34" stroke="#ccc" stroke-width="2"/>
  <text class="small-bold" x="120" y="228" text-anchor="middle" font-size="13">Metadata Reporting</text>

  <text class="heading-bold" x="126" y="277" text-anchor="middle">Customer’s Public</text>
  <rect x="30" y="292" width="196" height="103" rx="14" fill="url(#panelGrey)" stroke="#e8e8e8" stroke-width="4"/>
  <rect x="52" y="305" width="20" height="26" rx="2" fill="#444"/>
  <ellipse cx="66" cy="352" rx="14" ry="4" fill="#444"/><rect x="52" y="352" width="28" height="28" fill="#444"/>
  <text x="150" y="313" text-anchor="middle" fill="#444" font-size="10">VM / Physical</text>
  <text x="150" y="326" text-anchor="middle" fill="#444" font-size="10">Appliance</text>
  <rect x="128" y="334" width="42" height="18" fill="none" stroke="var(--orange)" stroke-width="1.5"/>
  <text x="150" y="367" text-anchor="middle" fill="#444" font-size="10">Read source data</text>
  <text x="150" y="380" text-anchor="middle" fill="#444" font-size="10">Tunnel Encryption</text>
  <text class="small-bold" x="122" y="422" text-anchor="middle" font-size="13">Metadata Reporting</text>

  <path d="M226,155 L309,190" stroke="#777" stroke-dasharray="3 3"/>
  <path d="M226,350 L298,317" stroke="#777" stroke-dasharray="3 3"/>
  <circle cx="309" cy="190" r="7" fill="var(--orange)"/>
  <circle cx="298" cy="317" r="7" fill="var(--orange)"/>

  <circle cx="423" cy="50" r="12" fill="#333"/><path d="M404,82 a19,16 0 0 1 38,0z" fill="#333"/>
  <circle cx="441" cy="55" r="8" fill="none" stroke="#333" stroke-width="4" stroke-dasharray="4 2"/>
  <text class="small-bold" x="426" y="105" text-anchor="middle" font-size="13">Administration Console</text>

  <circle cx="429" cy="267" r="140" fill="#ececec"/>
  <circle cx="429" cy="267" r="126" fill="var(--orange)"/>
  <circle cx="429" cy="267" r="108" fill="#f7f7f7"/>
  <text x="429" y="252" text-anchor="middle" fill="var(--ink)" font-weight="700" font-size="32" letter-spacing="2">TAVEXO</text>
  <text x="429" y="288" text-anchor="middle" fill="#444" font-weight="700" font-size="24">Indexing and</text>
  <text x="429" y="318" text-anchor="middle" fill="#444" font-weight="700" font-size="24">AI engine</text>

  <g class="certifications">
    <rect x="615" y="58" width="250" height="75" fill="#f1f1f1" stroke="#e5b9a3"/>
    <rect x="649" y="146" width="80" height="78" rx="6" fill="#3b2f5e"/>
    <rect x="756" y="146" width="80" height="78" fill="#1f5fae"/>
    <circle cx="683" cy="281" r="42" fill="#2c2f7a"/>
    <circle cx="788" cy="281" r="42" fill="#dfe9f3" stroke="#4a7fb5" stroke-width="3"/>
    <rect x="654" y="344" width="158" height="86" fill="#f4f4f4" stroke="#e5b9a3"/>
    <rect x="672" y="358" width="122" height="58" fill="#1d6d63"/>
  </g>

  <rect y="463" width="897" height="41" fill="var(--orange)"/>
  <polygon points="20,504 32,504 70,463 58,463" fill="#fff"/>
  <text class="footer-site" x="68" y="492">www.tavexo.com</text>
  <text class="footer-num" x="834" y="492">4</text>
</svg>
</section>

<!-- Lifecycle slide -->
<section class="slide slide--lifecycle">
<svg viewBox="0 0 897 504" aria-label="Lifecycle slide">
  <rect width="897" height="504" fill="var(--paper)"/>
  <polygon points="38,56 50,36 74,36 86,56 74,76 50,76" fill="#fff" stroke="#555" stroke-width="2"/>
  <polygon points="82,33 240,33 240,79 82,79 94,56" fill="var(--orange)"/>
  <text class="tag-text" x="100" y="64">Lifecycle</text>

  <g class="fan">
    <path d="M95,102 A170,170 0 0 1 265,272 L95,272 Z" fill="#8e8e8e"/>
    <path d="M95,272 L265,272 A170,170 0 0 1 95,442 Z" fill="#8e8e8e"/>
    <path d="M95,108 A164,164 0 0 1 211,156 L95,272 Z" fill="var(--orange)"/>
    <path d="M211,156 A164,164 0 0 1 259,272 L95,272 Z" fill="var(--orange)"/>
    <path d="M259,272 A164,164 0 0 1 211,388 L95,272 Z" fill="var(--orange)"/>
    <path d="M211,388 A164,164 0 0 1 95,436 L95,272 Z" fill="var(--orange)"/>
    <path d="M95,272L211,156M95,272L259,272M95,272L211,388" stroke="#fff" stroke-width="3"/>
    <ellipse cx="132" cy="150" rx="15" ry="5" fill="#fff"/><rect x="117" y="150" width="30" height="24" fill="#fff"/><path d="M117,158h30M117,166h30" stroke="var(--orange)" stroke-width="2"/>
    <rect x="185" y="208" width="22" height="28" rx="2" fill="#fff"/><path d="M189,218l3,3 5,-5M189,228l3,3 5,-5" stroke="var(--orange)" stroke-width="2" fill="none"/>
    <ellipse cx="204" cy="303" rx="15" ry="5" fill="#fff"/><rect x="189" y="303" width="30" height="24" fill="#fff"/><path d="M189,311h30M189,319h30" stroke="var(--orange)" stroke-width="2"/>
    <rect x="128" y="360" width="22" height="28" rx="2" fill="#fff"/><path d="M132,370l3,3 5,-5M132,380l3,3 5,-5" stroke="var(--orange)" stroke-width="2" fill="none"/>
    <circle cx="95" cy="272" r="62" fill="#eee"/>
    <circle cx="95" cy="272" r="56" fill="#fff"/>
    <text transform="translate(92,275) rotate(-90)" text-anchor="middle" fill="#333" font-weight="600" font-size="15">Unstructured</text>
    <text transform="translate(110,275) rotate(-90)" text-anchor="middle" fill="#333" font-weight="600" font-size="15">Data Siloes</text>
  </g>

  <g class="step">
    <path d="M352,190 a16,14 0 0 1 4,-26 a18,18 0 0 1 34,2 a14,14 0 0 1 4,24 z" fill="#333"/>
    <rect x="331" y="198" width="38" height="14" fill="#333"/><rect x="331" y="216" width="38" height="14" fill="#333"/>
    <rect x="383" y="198" width="38" height="14" fill="#333"/><rect x="383" y="216" width="38" height="14" fill="#333"/>
    <rect x="288" y="288" width="178" height="62" rx="8" fill="#fff" stroke="#999" stroke-width="2"/>
    <text class="box-label" x="377" y="326" text-anchor="middle">ROT Analysis</text>
  </g>
  <g class="step">
    <circle cx="567" cy="175" r="18" fill="#333"/>
    <path d="M533,235 a34,30 0 0 1 68,0z" fill="#333"/>
    <circle cx="550" cy="150" r="12" fill="none" stroke="#333" stroke-width="7" stroke-dasharray="5 3"/>
    <circle cx="598" cy="200" r="13" fill="none" stroke="#333" stroke-width="7" stroke-dasharray="5 3"/>
    <rect x="486" y="286" width="178" height="66" rx="8" fill="#fff" stroke="#999" stroke-width="2"/>
    <text class="box-label" x="575" y="314" text-anchor="middle">Automated</text>
    <text class="box-label" x="575" y="340" text-anchor="middle">Remediation</text>
  </g>
  <g class="step" stroke="#333" stroke-width="6">
    <path d="M765,188L740,162M765,188L795,160M765,188L735,215M765,188L790,220M765,188L765,150" fill="none"/>
    <circle cx="765" cy="188" r="17" fill="#333"/><circle cx="740" cy="162" r="8" fill="#333"/><circle cx="797" cy="158" r="11" fill="#333"/><circle cx="735" cy="215" r="6" fill="#333"/><circle cx="790" cy="220" r="6" fill="#333"/><circle cx="765" cy="148" r="6" fill="#333"/>
  </g>
  <g class="step">
    <rect x="686" y="268" width="178" height="102" rx="8" fill="#fff" stroke="#999" stroke-width="2"/>
    <text class="box-label" x="775" y="299" text-anchor="middle">Streamlined,</text>
    <text class="box-label" x="775" y="326" text-anchor="middle" textLength="160" lengthAdjust="spacingAndGlyphs">Controlled Data</text>
    <text class="box-label" x="775" y="353" text-anchor="middle">Storage</text>
  </g>

  <rect y="463" width="897" height="41" fill="var(--orange)"/>
  <polygon points="20,504 32,504 70,463 58,463" fill="#fff"/>
  <text class="footer-site" x="68" y="492">www.tavexo.com</text>
  <text class="footer-num" x="834" y="492">5</text>
</svg>
</section>

</div>
</body>
</html>
```